Ridgecrest Ag, LLC
Business cards, letterhead, envelopes
Project: Ridgecrest Ag, LLC
Ridgecrest Ag, LLC - Consulting
Creative Brief
Professional
Warren Colbeck
P.O. Box 517 Monterey, CA 93940
warren@ridgecrestag-example.com
1. I want to use my logo and will upload it. 2. I like clean, uncluttered design. 3. OK to think a little out of the box. 4. May be OK to use a different font than logo. 5. May be OK to use tagline "same dirt - new rules" differently (i.e., not right under Ridgecrest Ag as shown in logo).

```html
<!DOCTYPE html>
<html lang="en">
<head>
<meta charset="utf-8">
<title>Ridgecrest Ag — Business Cards</title>
<link rel="stylesheet" href="https://fonts.googleapis.com/css2?family=Arimo:wght@400;700&display=swap">
<style>
  :root {
    --board: #3c3c3c;
    --board-edge: #2a2a2a;
    --white: #ffffff;
    --maroon: #6b0f14;
    --mustard: #f8c25f;
    --ink: #1e1e1e;
    --bar-dark: #141414;
  }
  * { box-sizing: border-box; margin: 0; padding: 0; }
  html, body { width: 1200px; height: 1039px; overflow: hidden; }
  body {
    background: radial-gradient(ellipse at center, var(--board) 0%, var(--board-edge) 100%);
    font-family: "Arimo", Arial, sans-serif;
    position: relative;
  }
  .card {
    position: absolute;
    width: 478px;
    height: 270px;
    border-radius: 14px;
    box-shadow: 0 6px 14px rgba(0,0,0,.45);
    overflow: hidden;
  }
  .col-front { left: 108px; }
  .col-back { left: 597px; }
  .row-1 { top: 104px; }
  .row-2 { top: 386px; }
  .row-3 { top: 668px; }

  .theme-white { background: var(--white); color: var(--ink); --brand: var(--maroon); --bar: var(--maroon); }
  .theme-maroon { background: var(--maroon); color: var(--white); --brand: var(--white); --bar: var(--white); }
  .theme-mustard { background: var(--mustard); color: var(--white); --brand: var(--white); --bar: var(--bar-dark); }

  .brand { position: absolute; color: var(--brand); }
  .brand-name { font-weight: 700; letter-spacing: .5px; white-space: nowrap; line-height: 1; }
  .brand-tagline { letter-spacing: 1px; text-align: right; white-space: nowrap; }

  .front .brand { left: 26px; top: 58px; }
  .front .brand-name { font-size: 30px; }
  .front .brand-tagline { font-size: 9px; margin-top: 4px; }

  .contact {
    position: absolute;
    left: 0;
    top: 115px;
    padding: 8px 0 8px 18px;
    border-left: 10px solid var(--bar);
    font-size: 14px;
    line-height: 21px;
    font-style: normal;
  }
  .person {
    position: absolute;
    left: 243px;
    top: 155px;
    font-size: 18px;
    font-weight: 700;
    white-space: nowrap;
  }

  .back .brand {
    left: 50%;
    top: 135px;
    transform: translateX(-50%);
  }
  .back .brand-name { font-size: 46px; }
  .back .brand-tagline { font-size: 11px; margin-top: 6px; }
</style>
</head>
<body>

  <section class="card front theme-white col-front row-1">
    <div class="brand"><div class="brand-name">Ridgecrest Ag</div><div class="brand-tagline">ROOTED • FORWARD THINKING</div></div>
    <address class="contact">P.O. Box 517<br>Monterey, CA 93940<br>C:(831) 555-0142<br>F: (831) 555-0187<br>E: warren@ridgecrestag-example.com</address>
    <div class="person">Warren Colbeck</div>
  </section>
  <section class="card back theme-white col-back row-1">
    <div class="brand"><div class="brand-name">Ridgecrest Ag</div><div class="brand-tagline">ROOTED • FORWARD THINKING</div></div>
  </section>

  <section class="card front theme-maroon col-front row-2">
    <div class="brand"><div class="brand-name">Ridgecrest Ag</div><div class="brand-tagline">ROOTED • FORWARD THINKING</div></div>
    <address class="contact">P.O. Box 517<br>Monterey, CA 93940<br>C:(831) 555-0142<br>F: (831) 555-0187<br>E: warren@ridgecrestag-example.com</address>
    <div class="person">Warren Colbeck</div>
  </section>
  <section class="card back theme-maroon col-back row-2">
    <div class="brand"><div class="brand-name">Ridgecrest Ag</div><div class="brand-tagline">ROOTED • FORWARD THINKING</div></div>
  </section>

  <section class="card front theme-mustard col-front row-3">
    <div class="brand"><div class="brand-name">Ridgecrest Ag</div><div class="brand-tagline">ROOTED • FORWARD THINKING</div></div>
    <address class="contact">P.O. Box 517<br>Monterey, CA 93940<br>C:(831) 555-0142<br>F: (831) 555-0187<br>E: warren@ridgecrestag-example.com</address>
    <div class="person">Warren Colbeck</div>
  </section>
  <section class="card back theme-mustard col-back row-3">
    <div class="brand"><div class="brand-name">Ridgecrest Ag</div><div class="brand-tagline">ROOTED • FORWARD THINKING</div></div>
  </section>

</body>
</html>
```